We have developed a fully functional App called Corvalink. However, it requires a nicer GUI. You can see screenshots of our App on www.corvalink-example.com under "Tutorial". For those of you with Android, you can also install it. When you go to Corvalink-example.com, your phone will automatically redirect you to download. From there, you'll get a better idea of what our App looks like and how your design can make it way better. Please note we expect a design idea for most screens (there's about 8 screens) but do just one screen first and if you win, you can do the other 8 after.

Target Market(s)

People looking for dating / flirting

Industry/Entity Type

Android

Requirements
Must have
• sleek looking

```html
<!DOCTYPE html>
<html lang="en">
<head>
<meta charset="utf-8">
<title>Corvalink – Profile Screen</title>
<link rel="stylesheet" href="https://fonts.googleapis.com/css2?family=Ubuntu:wght@300;400&display=swap">
<style>
  :root {
    --page-bg: #f3f3f5;
    --status-bg: #1a1a1c;
    --status-icon: #33b5e5;
    --accent-line: #d66bd8;
    --text-main: #ffffff;
    --text-soft: rgba(255,255,255,0.62);
    --online: #8fd14f;
    --pin: #f2c14e;
    --info-bg: rgba(40, 28, 34, 0.55);
    --tags-bg: rgba(30, 22, 28, 0.72);
    --tag-divider: rgba(255,255,255,0.18);
    --btn-profile: #9a4cc6;
    --btn-photos: #b45dd0;
    --btn-favourite: #e66fa6;
    --btn-message: #dc5a92;
    --btn-icon: rgba(70, 20, 70, 0.45);
  }
  * { box-sizing: border-box; margin: 0; padding: 0; }
  html, body {
    width: 1200px; height: 1000px; overflow: hidden;
    background: var(--page-bg);
    font-family: "Ubuntu", "Helvetica Neue", Arial, sans-serif;
    font-weight: 300;
  }
  .screen {
    position: absolute; left: 350px; top: 55px;
    width: 500px; height: 890px;
    overflow: hidden; background: #000;
    box-shadow: 0 20px 50px rgba(0,0,0,0.18);
  }
  .status-bar {
    position: absolute; top: 0; left: 0; right: 0; height: 30px;
    background: var(--status-bg);
    border-bottom: 2px solid var(--accent-line);
    display: flex; align-items: center; justify-content: flex-end;
    gap: 5px; padding-right: 10px;
    color: var(--status-icon); font-size: 17px; font-weight: 400;
    z-index: 3;
  }
  .profile-photo {
    position: absolute; top: 30px; left: 0; right: 0; bottom: 145px;
    background:
      radial-gradient(ellipse 60% 45% at 25% 30%, #e9cfd2 0%, rgba(210,170,175,0.6) 45%, transparent 75%),
      radial-gradient(ellipse 45% 55% at 90% 75%, #3f8c95 0%, rgba(40,100,110,0.5) 50%, transparent 80%),
      linear-gradient(160deg, #b79ea2 0%, #6c5258 40%, #3a2a30 70%, #2c4f56 100%);
  }
  .top-actions {
    position: absolute; top: 58px; left: 22px; right: 26px;
    display: flex; justify-content: space-between; z-index: 2;
  }
  .name-row {
    position: absolute; top: 460px; left: 22px; right: 26px;
    display: flex; align-items: center; color: var(--text-main);
  }
  .online-dot {
    width: 14px; height: 14px; border-radius: 50%;
    border: 2px solid var(--online); margin-right: 12px;
  }
  .profile-name { font-size: 46px; flex: 1; }
  .profile-age { font-size: 36px; }
  .info-panel {
    position: absolute; top: 545px; left: 0; right: 0; height: 130px;
    background: var(--info-bg);
    border-top: 2px solid var(--accent-line);
    padding: 22px 26px 0 22px; color: var(--text-main);
  }
  .info-row { display: flex; justify-content: space-between; align-items: center; font-size: 24px; }
  .info-item { display: flex; align-items: center; gap: 10px; }
  .info-item .muted { color: var(--text-soft); }
  .chat-pref { margin-top: 24px; font-size: 16px; color: var(--text-soft); }
  .chat-pref strong { color: var(--text-main); font-weight: 400; }
  .interest-tags {
    position: absolute; top: 675px; left: 0; right: 0; height: 70px;
    background: var(--tags-bg);
    display: flex; align-items: center; list-style: none;
    font-size: 13px; letter-spacing: 0.3px; color: var(--text-soft);
  }
  .interest-tags li { padding: 0 16px; border-right: 1px solid var(--tag-divider); line-height: 40px; }
  .interest-tags li:first-child { padding-left: 22px; }
  .interest-tags li.more { border-right: none; color: var(--text-main); }
  .action-bar {
    position: absolute; left: 0; right: 0; bottom: 0; height: 145px;
    display: flex;
  }
  .action-bar button {
    flex: 1; border: none; display: flex; align-items: center; justify-content: center;
  }
  .btn-profile { background: var(--btn-profile); }
  .btn-photos { background: var(--btn-photos); }
  .btn-favourite { background: var(--btn-favourite); }
  .btn-message { background: var(--btn-message); }
</style>
</head>
<body>
<main class="screen">
  <div class="status-bar">
    <svg width="18" height="14" viewBox="0 0 18 14"><path d="M9 14 L0 4 A13 13 0 0 1 18 4 Z" fill="currentColor"/></svg>
    <svg width="12" height="14" viewBox="0 0 12 14"><path d="M0 14 L12 14 L12 0 Z" fill="currentColor"/></svg>
    <svg width="8" height="15" viewBox="0 0 8 15"><rect x="2" y="0" width="4" height="2" fill="currentColor"/><rect x="0" y="2" width="8" height="13" fill="currentColor"/></svg>
    <span class="clock">13:07</span>
  </div>

  <div class="profile-photo" role="img" aria-label="Profile photo of Jessica, wind-blown hair in soft pink and teal light"></div>

  <div class="top-actions">
    <svg width="20" height="30" viewBox="0 0 20 30"><path d="M15 4 L5 15 L15 26" fill="none" stroke="#fff" stroke-width="2"/></svg>
    <svg width="20" height="24" viewBox="0 0 20 24"><path d="M5 10 V6 A5 5 0 0 1 15 6" fill="none" stroke="#fff" stroke-width="1.8"/><rect x="2" y="10" width="16" height="12" rx="1.5" fill="none" stroke="#fff" stroke-width="1.8"/><rect x="9" y="14" width="2" height="4" fill="#fff"/></svg>
  </div>

  <div class="name-row">
    <span class="online-dot"></span>
    <h1 class="profile-name" style="font-weight:300">Jessica</h1>
    <span class="profile-age">23</span>
  </div>

  <section class="info-panel">
    <div class="info-row">
      <span class="info-item">
        <svg width="14" height="20" viewBox="0 0 14 20"><path d="M7 19 C2 12 1 9 1 7 A6 6 0 0 1 13 7 C13 9 12 12 7 19 Z" fill="none" stroke="var(--pin)" stroke-width="1.6"/><circle cx="7" cy="7" r="2" fill="none" stroke="var(--pin)" stroke-width="1.4"/></svg>
        Ottawa
      </span>
      <span class="info-item">
        <svg width="16" height="16" viewBox="0 0 16 16"><path d="M15 1 L1 7 L8 8 L9 15 Z" fill="none" stroke="var(--pin)" stroke-width="1.5" stroke-linejoin="round"/></svg>
        <span>3,2 km <span class="muted">away</span></span>
      </span>
    </div>
    <p class="chat-pref">Wants to chat with men <strong>20-25</strong></p>
  </section>

  <ul class="interest-tags">
    <li>VOLLEYBALL</li>
    <li>ANIMALS</li>
    <li>VEGETARIAN</li>
    <li>MATH</li>
    <li class="more">+24</li>
  </ul>

  <nav class="action-bar">
    <button class="btn-profile" aria-label="Profile">
      <svg width="36" height="42" viewBox="0 0 36 42"><path d="M18 3 A8 9 0 0 1 18 23 A8 9 0 0 1 18 3 Z M12 22 C5 25 3 30 3 38 H33 C33 30 31 25 24 22" fill="none" stroke="var(--btn-icon)" stroke-width="2"/></svg>
    </button>
    <button class="btn-photos" aria-label="Photos">
      <svg width="42" height="34" viewBox="0 0 42 34"><path d="M3 8 H12 L15 3 H27 L30 8 H39 V31 H3 Z" fill="none" stroke="var(--btn-icon)" stroke-width="2" stroke-linejoin="round"/><circle cx="21" cy="19" r="7" fill="none" stroke="var(--btn-icon)" stroke-width="2"/></svg>
    </button>
    <button class="btn-favourite" aria-label="Favourite">
      <svg width="38" height="36" viewBox="0 0 38 36"><path d="M19 2 L24 13 L36 14 L27 22 L30 34 L19 28 L8 34 L11 22 L2 14 L14 13 Z" fill="none" stroke="var(--btn-icon)" stroke-width="2" stroke-linejoin="round"/></svg>
    </button>
    <button class="btn-message" aria-label="Message">
      <svg width="40" height="30" viewBox="0 0 40 30"><rect x="2" y="2" width="36" height="26" fill="none" stroke="var(--btn-icon)" stroke-width="2"/><path d="M2 2 L20 17 L38 2" fill="none" stroke="var(--btn-icon)" stroke-width="2"/></svg>
    </button>
  </nav>
</main>
</body>
</html>
```